Business card design for Bront Engineering Qavo

We need a new business card design along with all the necessary to place an order. The company is Bront Engineering Qavo and we recently updated our logo.

```html
<!DOCTYPE html>
<html lang="en">
<head>
<meta charset="utf-8">
<title>Bront Engineering Qavo – Business Card</title>
<link href="https://fonts.googleapis.com/css2?family=Lato:wght@400;700;900&family=Montserrat:wght@600;700&display=swap" rel="stylesheet">
<style>
  :root{
    --stage:#1d1d1d;
    --ink:#121212;
    --paper:#ffffff;
    --gold:#e2bd22;
    --steel:#9a9a9a;
    --light:#f2f2f2;
  }
  *{margin:0;padding:0;box-sizing:border-box}
  html,body{width:1200px;height:1015px;overflow:hidden;background:var(--stage)}
  .canvas{position:relative;width:1200px;height:1015px}
  .card{position:absolute;left:250px;width:700px;height:400px;overflow:hidden}
  .card-back{top:45px;background:var(--ink)}
  .card-front{top:555px;background:var(--paper)}
  .bands{position:absolute;inset:0;width:700px;height:400px}
  .wordmark{position:absolute;display:flex;align-items:center;gap:14px;
    font-family:"Lato",sans-serif;font-weight:900;font-size:40px;letter-spacing:1px;white-space:nowrap}
  .wordmark .mark-square{width:20px;height:20px;background:var(--gold)}
  .card-back .wordmark{left:0;right:0;top:125px;justify-content:center;color:var(--steel)}
  .card-front .wordmark{left:0;right:0;top:95px;justify-content:center;color:var(--steel)}
  .identity{position:absolute;left:170px;top:312px;text-align:right;width:200px}
  .identity .name{font-family:"Montserrat",sans-serif;font-weight:700;font-size:22px;color:var(--gold);letter-spacing:.5px}
  .identity .role{font-family:"Lato",sans-serif;font-size:15px;color:var(--light);margin-top:2px}
  .divider{position:absolute;left:390px;top:305px;width:1px;height:62px;background:var(--gold);opacity:.6}
  .contacts{position:absolute;left:405px;top:300px;list-style:none;
    font-family:"Lato",sans-serif;font-size:15px;color:var(--light)}
  .contacts li{display:flex;align-items:center;gap:8px;height:22px}
  .contacts svg{width:15px;height:15px;fill:none;stroke:var(--gold);stroke-width:2}
  .address{position:absolute;left:170px;top:372px;font-family:"Lato",sans-serif;font-size:14px;color:var(--light)}
</style>
</head>
<body>
<main class="canvas">

  <section class="card card-back" aria-label="Card back">
    <svg class="bands" viewBox="0 0 700 400" aria-hidden="true">
      <polygon points="0,355 300,355 330,320 700,320 700,328 338,328 308,368 0,368" fill="var(--gold)"/>
      <polygon points="0,368 308,368 338,328 700,328 700,400 0,400" fill="var(--ink)"/>
      <polygon points="0,360 0,400 0,400" fill="var(--ink)"/>
      <polygon points="318,318 334,302 700,302 700,310 340,310 326,318" fill="var(--steel)"/>
    </svg>
    <div class="wordmark"><span class="mark-square"></span>Bront Engineering Qavo</div>
  </section>

  <section class="card card-front" aria-label="Card front">
    <svg class="bands" viewBox="0 0 700 400" aria-hidden="true">
      <polygon points="0,255 0,400 700,400 700,190 400,190 370,230 0,230" fill="var(--ink)"/>
      <polygon points="0,218 360,218 390,178 700,178 700,190 400,190 370,230 0,230" fill="var(--gold)" transform="translate(0,-14)"/>
      <polygon points="0,230 370,230 400,190 700,190 700,176 392,176 362,216 0,216" fill="var(--gold)"/>
      <polygon points="376,212 396,186 402,186 382,212" fill="none"/>
      <polygon points="382,206 402,164 700,164 700,172 408,172 390,206" fill="var(--steel)"/>
    </svg>
    <div class="wordmark"><span class="mark-square"></span>Bront Engineering Qavo</div>

    <div class="identity">
      <div class="name">DANIEL CARVER</div>
      <div class="role">Managing Director</div>
    </div>
    <div class="divider"></div>
    <ul class="contacts">
      <li><svg viewBox="0 0 24 24"><path d="M5 3h4l2 5-3 2a12 12 0 0 0 6 6l2-3 5 2v4a2 2 0 0 1-2 2A18 18 0 0 1 3 5a2 2 0 0 1 2-2z"/></svg>044-870 315 642</li>
      <li><svg viewBox="0 0 24 24"><rect x="2" y="5" width="20" height="14"/><path d="M2 5l10 8 10-8"/></svg>info@brontqavo.com</li>
      <li><svg viewBox="0 0 24 24"><circle cx="12" cy="12" r="10"/><path d="M2 12h20M12 2c3 3 3 17 0 20M12 2c-3 3-3 17 0 20"/></svg>www.brontqavo.com</li>
    </ul>
    <div class="address">87, Harbor Road, Lindale Heights, 30418</div>
  </section>

</main>
</body>
</html>
```